Design for web based travel expence program

We need a design template for a web based travel expence program we have created. The current design is based on a standard framework, and it needs to be "spiced" up.
Please notice that there are only 3-4 screen shots that needs an "upspice" of the design. No complete web design is expected for this price. For the right designer we have many more jobs coming up!
Tovalin Accounting is a Scandinavian accounting company with offices in Norway (Oslo) and Stockholm (Sweden). Our goal is to be a proactive accounting company known for trouble-free solutions and wide knowledge about what we do. We have created an "easy" accounting program enabling clients to take picture of vouchers, upload them to our portal and gather them to a travel expense scheme that can be approved and sent directly into an accounting program.
The program is pure web based and created with sophisticated programming code, but only with a standard framework as design template. We need a touch of professional design that easily can be implemented “on top” of the framework.
We are thinking that the designer should add icons and create the squared elements a bit rounder and with a more beautiful touch.
We are looking for a designer that preferably can create CSS files with an improved design, though the first step should be to create some pictures/Photshop examples on how it could look like. The files we have uploaded are the screen shots that needs to be improved with a better design.
Reason: Thank you for the designs, but still a bit few to choose between.
Target Market(s)
All type of businesses, but the end user is in focus. The program is designed to be easy-to-learn and very useful for all persons dealing with travel expence forms.
Industry/Entity Type
Accounting

```html
<!DOCTYPE html>
<html lang="no">
<head>
<meta charset="utf-8">
<title>Utleggjuni – reiseregning</title>
<link rel="stylesheet" href="https://fonts.googleapis.com/css2?family=Open+Sans:wght@400;600;700&display=swap">
<style>
:root{
  --page:#f1f1f1;
  --card:#ffffff;
  --line:#e2e2e2;
  --ink:#1f1f1f;
  --muted:#9a9a9a;
  --blue:#34a9dd;
  --blue-dark:#1f8fc4;
  --orange:#f0a73e;
  --orange-dark:#d48a22;
  --slate:#3a4250;
  --slate-dark:#262c36;
  --icon:#7a7a7a;
}
*{box-sizing:border-box;margin:0;padding:0}
html,body{width:1200px;height:791px;overflow:hidden}
body{background:var(--page);font-family:"Open Sans",Arial,sans-serif;color:var(--ink);position:relative}
.topbar{position:absolute;left:0;top:0;width:1200px;height:71px;background:var(--card);box-shadow:0 2px 4px rgba(0,0,0,.12)}
.topbar h1{position:absolute;left:95px;top:10px;font-size:29px;font-weight:700;letter-spacing:.5px}
.topbar .status{position:absolute;right:95px;top:15px;font-size:18px;color:var(--muted)}
.btn{display:inline-flex;align-items:center;justify-content:center;border-radius:4px;font-size:13px;color:#fff;font-weight:600;border:1px solid transparent}
.btn-orange{background:linear-gradient(#f4b24f,var(--orange));border-color:var(--orange-dark)}
.btn-blue{background:linear-gradient(#45b6e6,var(--blue));border-color:var(--blue-dark)}
.btn-slate{background:linear-gradient(#4a5363,var(--slate));border-color:var(--slate-dark)}
.btn-ghost{background:#fff;border-color:#d6d6d6;color:#555;font-weight:400}
.back{position:absolute;left:95px;top:89px;width:181px;height:29px}
.back::before{content:"";border:4px solid transparent;border-right:5px solid #fff;border-left:0;margin-right:7px}
.crumbs{position:absolute;right:95px;top:96px;font-size:13px;color:#333}
.crumbs a{color:var(--blue);text-decoration:none}
.card{position:absolute;background:var(--card);border-radius:4px;box-shadow:0 1px 3px rgba(0,0,0,.13)}
.label{font-size:13px;color:#333}
.field{position:absolute;height:37px;border:1px solid #d8d8d8;border-radius:6px;background:#fff;font-size:13px;color:#666;padding-left:16px;display:flex;align-items:center}
.field.date{color:#888;font-size:12px}
.field.date::after{content:"";position:absolute;right:11px;top:15px;border:5px solid transparent;border-top:7px solid #888;border-bottom:0}
.card h2{font-size:17px;font-weight:400;position:absolute;left:18px}
.title-card{left:95px;top:135px;width:755px;height:143px}
.side-card{left:861px;top:135px;width:244px;height:143px}
.side-card .btn{position:absolute;left:34px;width:180px;height:29px}
.receipts-card{left:95px;top:293px;width:1010px;height:83px}
.stats{position:absolute;left:18px;top:49px;font-size:13px}
.stats b{font-weight:400;color:var(--blue)}
.trip-card{left:95px;top:391px;width:1010px;height:165px}
.trip-card .label{position:absolute;top:43px}
.trip-card .btn{position:absolute;top:120px;height:30px}
.rates{position:absolute;left:19px;top:118px;font-size:14px;color:var(--blue);line-height:1.3}
.rates span{display:block;color:#222;font-size:13px}
.avail{position:absolute;left:95px;top:574px;font-size:17px}
.voucher{top:605px;width:245px;height:173px}
.voucher .name{position:absolute;left:17px;top:14px;font-size:14px;color:#444}
.row{position:absolute;left:0;width:100%;height:41px;display:flex;align-items:center;padding-left:16px;font-size:13px;border-top:1px solid var(--line)}
.row:first-of-type{border-top:0}
.row svg{width:24px;height:28px;margin-right:14px}
</style>
</head>
<body>
<header class="topbar">
  <h1>UTLEGGJUNI</h1>
  <div class="status">Status: ikke sendt</div>
</header>

<a class="btn btn-orange back">Lagre og tilbake</a>
<nav class="crumbs">Lag refusion&nbsp; / &nbsp;<a>Send</a></nav>

<section class="card title-card">
  <div class="label" style="position:absolute;left:19px;top:15px;font-size:14px">Title</div>
  <div class="field" style="left:18px;top:46px;width:724px;height:46px">Utleggjuni</div>
</section>

<aside class="card side-card">
  <a class="btn btn-blue" style="top:18px">Kvitteringer</a>
  <a class="btn btn-slate" style="top:57px">Reiseregning</a>
  <a class="btn btn-ghost" style="top:96px">Reiseregning</a>
</aside>

<section class="card receipts-card">
  <h2 style="top:13px">Kvitteringer</h2>
  <div class="stats">Antall : <b>3</b>&nbsp;&nbsp;&nbsp;&nbsp; Belop : <b>804</b></div>
  <a class="btn btn-blue" style="position:absolute;right:15px;top:27px;width:132px;height:31px">Velg kvitteringer</a>
</section>

<section class="card trip-card">
  <h2 style="top:13px">Reise</h2>
  <div class="label" style="left:18px">Formal</div>
  <div class="label" style="left:265px">Destination</div>
  <div class="label" style="left:511px">Fra</div>
  <div class="label" style="left:759px">Til</div>
  <div class="field" style="left:18px;top:67px;width:237px"></div>
  <div class="field" style="left:265px;top:67px;width:237px"></div>
  <div class="field date" style="left:511px;top:67px;width:237px">mm/dd/yyyy</div>
  <div class="field date" style="left:759px;top:67px;width:237px">mm/dd/yyyy</div>
  <div class="rates">States satser<span>Belop:0</span></div>
  <a class="btn btn-orange" style="left:128px;width:151px">Beregn automatisk</a>
  <a class="btn btn-orange" style="left:287px;width:101px">Velg saster</a>
  <a class="btn btn-blue" style="left:763px;width:55px">Slett</a>
  <a class="btn btn-slate" style="left:825px;width:166px">Forhandsvis og send</a>
</section>

<h3 class="avail" style="font-weight:400">Ledige kvitteringer</h3>

<svg width="0" height="0" style="position:absolute">
  <defs>
    <g id="ico-cal"><rect x="1" y="4" width="22" height="22" rx="2" fill="none" stroke="#7a7a7a" stroke-width="2"/><rect x="1" y="4" width="22" height="6" fill="#7a7a7a"/><rect x="5" y="1" width="3" height="6" fill="#7a7a7a"/><rect x="16" y="1" width="3" height="6" fill="#7a7a7a"/><g fill="#7a7a7a"><rect x="5" y="13" width="3" height="3"/><rect x="10.5" y="13" width="3" height="3"/><rect x="16" y="13" width="3" height="3"/><rect x="5" y="19" width="3" height="3"/><rect x="10.5" y="19" width="3" height="3"/><rect x="16" y="19" width="3" height="3"/></g></g>
    <g id="ico-doc"><path d="M2 1h13l7 7v19H2z M15 1v7h7" fill="none" stroke="#7a7a7a" stroke-width="1.3" stroke-linejoin="round"/></g>
    <g id="ico-txt"><path d="M2 1h13l7 7v19H2z M15 1v7h7" fill="none" stroke="#7a7a7a" stroke-width="1.3" stroke-linejoin="round"/><path d="M6 13h12M6 17h12M6 21h9" stroke="#7a7a7a" stroke-width="1.5"/></g>
  </defs>
</svg>

<article class="card voucher" style="left:95px">
  <div class="name">Elektronikk</div>
  <div class="row" style="top:46px"><svg viewBox="0 0 24 28"><use href="#ico-cal"/></svg>2013-03-08</div>
  <div class="row" style="top:87px;border-top:1px solid var(--line)"><svg viewBox="0 0 24 28"><use href="#ico-doc"/></svg>100</div>
  <div class="row" style="top:128px;border-top:1px solid var(--line)"><svg viewBox="0 0 24 28"><use href="#ico-txt"/></svg>20</div>
</article>
<article class="card voucher" style="left:350px">
  <div class="name">Elektronikk</div>
  <div class="row" style="top:46px"><svg viewBox="0 0 24 28"><use href="#ico-cal"/></svg>2013-03-08</div>
  <div class="row" style="top:87px;border-top:1px solid var(--line)"><svg viewBox="0 0 24 28"><use href="#ico-doc"/></svg>100</div>
  <div class="row" style="top:128px;border-top:1px solid var(--line)"><svg viewBox="0 0 24 28"><use href="#ico-txt"/></svg>20</div>
</article>
<article class="card voucher" style="left:605px">
  <div class="name">Elektronikk</div>
  <div class="row" style="top:46px"><svg viewBox="0 0 24 28"><use href="#ico-cal"/></svg>2013-03-08</div>
  <div class="row" style="top:87px;border-top:1px solid var(--line)"><svg viewBox="0 0 24 28"><use href="#ico-doc"/></svg>100</div>
  <div class="row" style="top:128px;border-top:1px solid var(--line)"><svg viewBox="0 0 24 28"><use href="#ico-txt"/></svg>20</div>
</article>
<article class="card voucher" style="left:860px">
  <div class="name">Elektronikk</div>
  <div class="row" style="top:46px"><svg viewBox="0 0 24 28"><use href="#ico-cal"/></svg>2013-03-08</div>
  <div class="row" style="top:87px;border-top:1px solid var(--line)"><svg viewBox="0 0 24 28"><use href="#ico-doc"/></svg>100</div>
  <div class="row" style="top:128px;border-top:1px solid var(--line)"><svg viewBox="0 0 24 28"><use href="#ico-txt"/></svg>20</div>
</article>
</body>
</html>
```